Building Company Business Card Design

Need a design for a business card:
It needs to have: Name, Phone, Facebook link, Website, email
i would also like a list of works we undertake:
-New Homes
-Extensions, Renovations & Bathrooms
-Decking, Carports, Sheds (Residential and Industrial)
-Carpentry
-Fences, Patios & Pergolas

Name, Phone, Facebook link, Website, email + details of services provided listed in description

```html
<!DOCTYPE html>
<html lang="en">
<head>
<meta charset="utf-8">
<title>Northgate Homes – Business Card</title>
<link href="https://fonts.googleapis.com/css2?family=Roboto:wght@300;400;500;700&family=Montserrat:wght@600&display=swap" rel="stylesheet">
<style>
  :root {
    --stage: #121212;
    --green: #3cb54a;
    --green-deep: #27a246;
    --green-light: #8ccd6a;
    --white: #ffffff;
    --ink: #1f1f1f;
    --grey: #7e7e7e;
  }
  * { margin: 0; padding: 0; box-sizing: border-box; }
  html, body { width: 1200px; height: 960px; overflow: hidden; }
  body {
    background: var(--stage);
    font-family: "Roboto", sans-serif;
    position: relative;
  }
  .card {
    position: absolute;
    left: 249px;
    width: 702px;
    height: 401px;
    box-shadow: 0 10px 24px rgba(0,0,0,.55);
    overflow: hidden;
  }
  /* Front */
  .card-front { top: 60px; background: var(--green); }
  .front-art {
    position: absolute;
    left: 0; top: 0;
    width: 500px; height: 401px;
    background: linear-gradient(120deg, var(--green-deep) 0%, var(--green-light) 45%, var(--green-deep) 80%, var(--green) 100%);
    clip-path: polygon(0 0, 255px 0, 500px 401px, 0 401px);
  }
  .front-brand {
    position: absolute;
    right: 31px;
    top: 350px;
    color: var(--white);
    font-family: "Montserrat", sans-serif;
    font-weight: 600;
    text-align: center;
    line-height: 1;
  }
  .front-brand .brand-main { display: block; font-size: 19px; letter-spacing: .2px; }
  .front-brand .brand-sub { display: block; font-size: 9.3px; margin-top: 2px; letter-spacing: .1px; }

  /* Back */
  .card-back { top: 500px; background: var(--white); }
  .side-bar {
    position: absolute;
    top: 100px;
    width: 16px; height: 200px;
    background: var(--green);
  }
  .side-bar.left { left: 0; }
  .side-bar.right { right: 0; }
  .divider {
    position: absolute;
    left: 350px; top: 93px;
    width: 1px; height: 214px;
    background: var(--green);
    opacity: .7;
  }
  .back-brand {
    position: absolute;
    left: 40px; top: 172px;
    width: 260px;
    display: flex; align-items: center; gap: 10px;
    color: var(--green);
    font-weight: 700;
    font-size: 26px;
    line-height: 1.05;
  }
  .back-brand .brand-square {
    width: 30px; height: 30px;
    background: var(--green);
    flex-shrink: 0;
  }
  .person { position: absolute; left: 402px; top: 110px; }
  .person-name { font-size: 35px; line-height: 1; letter-spacing: .3px; }
  .person-name .first { color: var(--green); font-weight: 700; }
  .person-name .last { color: var(--grey); font-weight: 300; }
  .person-role { font-size: 17px; color: var(--ink); margin-top: 3px; letter-spacing: .3px; }
  .contacts { position: absolute; left: 402px; top: 191px; list-style: none; }
  .contacts li {
    display: flex; align-items: center;
    height: 24px;
    font-size: 15.5px; color: var(--ink); letter-spacing: .4px;
  }
  .contacts svg { width: 16px; height: 16px; margin-right: 10px; flex-shrink: 0; }
  .services {
    position: absolute;
    left: 0; right: 0; top: 313px;
    text-align: center;
  }
  .services h2 {
    font-size: 17.5px; font-weight: 500; color: var(--green);
    letter-spacing: .3px; line-height: 1;
  }
  .services ul { list-style: none; margin-top: 6px; }
  .services li {
    display: inline-flex; align-items: center;
    font-size: 15.5px; color: var(--ink); letter-spacing: .3px;
    margin: 0 2px;
  }
  .services li::before {
    content: "";
    width: 10px; height: 10px; border-radius: 50%;
    background: var(--green);
    margin-right: 7px;
  }
  .services .row { line-height: 24px; }
</style>
</head>
<body>

<section class="card card-front">
  <div class="front-art" role="img" aria-label="Large angled roof-shape decoration in light and deep greens"></div>
  <div class="front-brand">
    <span class="brand-main">NORTHGATE HOMES</span>
    <span class="brand-sub">AND DEVELOPMENTS PTY LTD</span>
  </div>
</section>

<section class="card card-back">
  <div class="side-bar left"></div>
  <div class="side-bar right"></div>

  <div class="back-brand">
    <span class="brand-square"></span>
    <span>Northgate Homes</span>
  </div>

  <div class="divider"></div>

  <div class="person">
    <h1 class="person-name"><span class="first">Marta</span> <span class="last">Kovar</span></h1>
    <p class="person-role">Founder &amp; CEO</p>
  </div>

  <ul class="contacts">
    <li>
      <svg viewBox="0 0 16 16"><path d="M4 2l2 3-1.4 1.4c.8 1.8 2.2 3.2 4 4L10 9l3 2-1 2.5C7 13.5 2.5 9 2.5 4z" fill="none" stroke="#3cb54a" stroke-width="1.4" stroke-linejoin="round"/><path d="M10 2.5a4 4 0 0 1 3.5 3.5M10 5a1.5 1.5 0 0 1 1 1" fill="none" stroke="#3cb54a" stroke-width="1.2"/></svg>
      (555) 014-2730
    </li>
    <li>
      <svg viewBox="0 0 16 16"><circle cx="8" cy="8" r="8" fill="#3cb54a"/></svg>
      @facebook.com
    </li>
    <li>
      <svg viewBox="0 0 16 16"><circle cx="8" cy="8" r="7" fill="none" stroke="#3cb54a" stroke-width="1.4"/><ellipse cx="8" cy="8" rx="3" ry="7" fill="none" stroke="#3cb54a" stroke-width="1.1"/><path d="M1 8h14" stroke="#3cb54a" stroke-width="1.1"/></svg>
      www.yourwebsite.com
    </li>
    <li>
      <svg viewBox="0 0 16 16"><rect x="1.5" y="5" width="13" height="9" fill="none" stroke="#3cb54a" stroke-width="1.4"/><path d="M1.5 5l6.5 5 6.5-5M8 1.5l-3 3.5M8 1.5l3 3.5" fill="none" stroke="#3cb54a" stroke-width="1.2"/></svg>
      info@yourwebsite.com
    </li>
  </ul>

  <div class="services">
    <h2>SERVICES</h2>
    <ul>
      <div class="row">
        <li>New Homes</li>
        <li>Extensions, Renovations &amp; Bathrooms</li>
        <li>Carpentry</li>
      </div>
      <div class="row">
        <li>Decking, Carports, Sheds (Residential and Industrial)</li>
        <li>Fences, Patios &amp; Pergolas</li>
      </div>
    </ul>
  </div>
</section>

</body>
</html>
```